New website for actress www.marlene-vogtberg.de

My website is a little old and needs a new look.
I am a german actress who is in the TV and Theaterbusiness.
my chirpnet account is called MarVogtberg
this design will be set up as wordpress site and needs to be optimized for mobile,
so please provide mobile screen views too.
the content will not change much from the excisting site but I would like to have a news section with Videos and press Releases
I would also like my chirpnet feed to be displayed on my landing page.
I am looking forward to your ideas
best regards
marlene

Target Market(s)

press and fans

Industry/Entity Type

Tv

Font styles to use
Serif
Sans Serif

Colors

Designer to choose colors to be used in the design.

Requirements
Must have
• see above

```html
<!DOCTYPE html>
<html lang="de">
<head>
<meta charset="utf-8">
<title>Marlene Vogtberg</title>
<link href="https://fonts.googleapis.com/css2?family=Open+Sans:wght@400;600;700&display=swap" rel="stylesheet">
<style>
  :root{
    --page:#4b4b4b;
    --pink:#e0177a;
    --black:#0c0c0c;
    --white:#ffffff;
    --text:#6b6b6b;
    --grey-box:#e1e1e1;
    --rule:#e6e6e6;
    --blue:#1a9ad6;
  }
  *{box-sizing:border-box;margin:0;padding:0}
  html,body{width:849px;height:1200px;overflow:hidden}
  body{
    background:var(--page);
    background-image:repeating-linear-gradient(0deg,rgba(255,255,255,.025) 0 1px,transparent 1px 3px),
                     repeating-linear-gradient(90deg,rgba(0,0,0,.05) 0 1px,transparent 1px 3px);
    font-family:"Open Sans",Arial,sans-serif;
    position:relative;
  }
  .site-header{position:absolute;top:14px;left:0;width:849px;height:54px;display:flex;align-items:center;justify-content:center;gap:16px}
  .flourish{width:112px;height:30px;background:linear-gradient(90deg,transparent,rgba(255,255,255,.55),transparent);border-radius:15px;opacity:.7}
  .site-title{color:var(--pink);font-weight:700;font-size:27px;letter-spacing:.2px}
  .main-nav{position:absolute;top:74px;left:86px;width:679px;height:42px;background:var(--black);border-radius:3px 3px 0 0;display:flex;align-items:center;justify-content:space-between;padding:0 15px 0 13px}
  .main-nav a{color:#fff;text-decoration:none;font-size:9px;font-weight:600;line-height:18px;white-space:nowrap;flex:1 1 auto;text-align:center;border-left:1px solid #555}
  .main-nav a:first-child{border-left:0;color:var(--pink);text-align:left;flex:0 0 auto;padding-right:11px}
  .main-nav a:last-child{text-align:right;flex:0 0 auto;padding-left:13px}
  .hero{position:absolute;top:116px;left:86px;width:679px;height:274px;background:linear-gradient(90deg,#c73a55,#d85a70 40%,#c83c56)}
  .hero-strip{position:absolute;top:390px;left:86px;width:679px;height:80px;background:linear-gradient(90deg,#2a2228,#3a2f38 50%,#2a2228);display:flex;align-items:center;justify-content:center;gap:12px}
  .thumb{width:66px;height:66px;border-radius:50%;background:radial-gradient(circle at 50% 40%,#f0d2b4,#caa070 60%,#7b5a48)}
  .strip-arrow{position:absolute;top:17px;width:24px;height:44px;background:rgba(255,255,255,.35);display:flex;align-items:center;justify-content:center}
  .strip-arrow.left{left:0;border-radius:0 22px 22px 0}
  .strip-arrow.right{right:0;border-radius:22px 0 0 22px}
  .content{position:absolute;top:482px;left:86px;width:679px;height:610px;background:var(--white);box-shadow:0 14px 18px -10px rgba(0,0,0,.6)}
  .content::before,.content::after{content:"";position:absolute;left:0;width:100%;height:6px;background-size:6px 6px;background-repeat:repeat-x}
  .content::before{top:-6px;background-image:linear-gradient(-45deg,var(--white) 3px,transparent 0),linear-gradient(45deg,var(--white) 3px,transparent 0);background-position:bottom}
  .content::after{bottom:-6px;background-image:linear-gradient(-135deg,var(--white) 3px,transparent 0),linear-gradient(135deg,var(--white) 3px,transparent 0);background-position:top}
  .section-title{color:var(--pink);font-weight:400;font-size:20px;text-align:center;letter-spacing:.3px}
  .welcome{position:absolute;top:42px;left:0;width:100%}
  .welcome p{color:var(--text);font-size:12.2px;line-height:14px;text-align:center;width:590px;margin:15px auto 0}
  .welcome p+p{margin-top:15px}
  .divider{position:absolute;top:193px;left:126px;width:426px;height:1px;background:var(--rule)}
  .videos{position:absolute;top:208px;left:0;width:100%}
  .video-row{position:absolute;top:38px;left:77px;width:526px;height:84px;display:flex;gap:5px;align-items:flex-start}
  .video{width:128px;height:84px;flex:none;position:relative;box-shadow:0 4px 4px -2px rgba(0,0,0,.35)}
  .video.outdoor{background:linear-gradient(135deg,#6d5a4a,#a08670)}
  .video.studio{background:linear-gradient(135deg,#8aa6c0,#b8cad8)}
  .video.premiere{background:linear-gradient(135deg,#6d9a3c,#9cbf55)}
  .video.gala{background:linear-gradient(135deg,#e7e9ee,#b8c6d2)}
  .play{position:absolute;left:50%;top:50%;width:24px;height:24px;margin:-12px 0 0 -12px}
  .gallery-arrow{position:absolute;top:31px}
  .gallery-arrow.left{left:-22px}.gallery-arrow.right{right:-22px}
  .tweets{position:absolute;top:382px;left:59px;width:558px}
  .tweets-heading{display:flex;align-items:center;gap:6px;color:var(--blue);font-size:9.5px;font-weight:700}
  .tweets-heading .dot{width:13px;height:13px;border-radius:50%;background:var(--blue)}
  .tweet-row{display:flex;gap:3px;margin-top:9px}
  .tweet{width:277px;height:100px;background:var(--grey-box);display:flex;padding:24px 15px 0 16px;gap:8px}
  .avatar{width:38px;height:38px;flex:none;background:linear-gradient(135deg,#9a6a48,#d9b08c)}
  .tweet h3{color:var(--pink);font-size:10.5px;font-weight:600;margin-bottom:3px}
  .tweet p{color:#777;font-size:9.4px;line-height:11.4px}
  .more{display:block;text-align:right;color:var(--pink);font-size:9px;margin-top:6px;text-decoration:none}
  .closing-rule{position:absolute;top:555px;left:229px;width:221px;height:1px;background:#9a9a9a}
  .closing-rule::after{content:"";position:absolute;left:92px;top:-5px;width:37px;height:10px;border-radius:50%;border:1px solid #9a9a9a;background:var(--white)}
  .site-footer{position:absolute;top:1112px;left:0;width:849px;text-align:center;color:#fff;font-size:8.8px}
  .social{display:flex;justify-content:center;gap:4px;margin-top:14px}
  .social span{width:24px;height:24px;border-radius:50%}
  .social .facepage{background:#a8174c}
  .social .chirpnet{background:#2aa3cf}
  .social .globecircle{background:#d3393f}
</style>
</head>
<body>
  <header class="site-header">
    <div class="flourish" role="img" aria-label="Ornamental flourish"></div>
    <h1 class="site-title">Marlene Vogtberg</h1>
    <div class="flourish" role="img" aria-label="Ornamental flourish"></div>
  </header>

  <nav class="main-nav">
    <a href="#">HOME</a><a href="#">BIOGRAPHIE</a><a href="#">INTERVIEW</a><a href="#">THEATERFOTOS</a><a href="#">PRIVATFOTOS</a><a href="#">EROTIKFOTOS</a><a href="#">AUTOGRAMME</a><a href="#">CHARITY</a><a href="#">KONTAKT</a>
  </nav>

  <div class="hero" role="img" aria-label="Portrait photo of the actress at a red-carpet event"></div>
  <div class="hero-strip">
    <span class="strip-arrow left"><svg width="8" height="16" viewBox="0 0 8 16"><path d="M7 1 1 8l6 7" fill="none" stroke="#999" stroke-width="1"/></svg></span>
    <span class="thumb" role="img" aria-label="Slide thumbnail photo"></span>
    <span class="thumb" role="img" aria-label="Slide thumbnail photo"></span>
    <span class="thumb" role="img" aria-label="Slide thumbnail photo"></span>
    <span class="thumb" role="img" aria-label="Slide thumbnail photo"></span>
    <span class="thumb" role="img" aria-label="Slide thumbnail photo"></span>
    <span class="thumb" role="img" aria-label="Slide thumbnail photo"></span>
    <span class="strip-arrow right"><svg width="8" height="16" viewBox="0 0 8 16"><path d="M1 1l6 7-6 7" fill="none" stroke="#999" stroke-width="1"/></svg></span>
  </div>

  <main class="content">
    <section class="welcome">
      <h2 class="section-title">HALLO UND HERZLICH WILLKOMMEN</h2>
      <p>in meiner Welt. Hier findet Ihr Augenblicke meiner Arbeit, Einblicke in meine ganz privaten Ansichten und Ausblicke auf meine aktuellen Projekte für Fernsehen, Theater, Film und mehr. Einfach auf die gewünschte Rubrik klicken und schon zeige ich, was dahintersteckt.</p>
      <p>Viel Spaß beim Blick hinter die Kulissen!</p>
    </section>
    <div class="divider"></div>

    <section class="videos">
      <h2 class="section-title">VIDEO GALLERY</h2>
      <div class="video-row">
        <svg class="gallery-arrow left" width="12" height="22" viewBox="0 0 12 22"><path d="M11 1 1 11l10 10" fill="none" stroke="#555" stroke-width="1.2"/></svg>
        <div class="video outdoor" role="img" aria-label="Video still of the actress outdoors"><svg class="play" viewBox="0 0 24 24"><circle cx="12" cy="12" r="11" fill="rgba(0,0,0,.3)" stroke="#fff" stroke-width="1.5"/><path d="M9.5 7.5v9l7-4.5z" fill="#fff"/></svg></div>
        <div class="video studio" role="img" aria-label="Video still of the actress in studio"><svg class="play" viewBox="0 0 24 24"><circle cx="12" cy="12" r="11" fill="rgba(0,0,0,.3)" stroke="#fff" stroke-width="1.5"/><path d="M9.5 7.5v9l7-4.5z" fill="#fff"/></svg></div>
        <div class="video premiere" role="img" aria-label="Video still from a musical premiere"><svg class="play" viewBox="0 0 24 24"><circle cx="12" cy="12" r="11" fill="rgba(0,0,0,.3)" stroke="#fff" stroke-width="1.5"/><path d="M9.5 7.5v9l7-4.5z" fill="#fff"/></svg></div>
        <div class="video gala" role="img" aria-label="Video still from a gala event"><svg class="play" viewBox="0 0 24 24"><circle cx="12" cy="12" r="11" fill="rgba(0,0,0,.3)" stroke="#fff" stroke-width="1.5"/><path d="M9.5 7.5v9l7-4.5z" fill="#fff"/></svg></div>
        <svg class="gallery-arrow right" width="12" height="22" viewBox="0 0 12 22"><path d="M1 1l10 10L1 21" fill="none" stroke="#555" stroke-width="1.2"/></svg>
      </div>
    </section>

    <section class="tweets">
      <div class="tweets-heading">LATES TWEETS <span class="dot"></span></div>
      <div class="tweet-row">
        <article class="tweet">
          <div class="avatar" role="img" aria-label="Profile photo"></div>
          <div><h3>Nina Falkner</h3><p>Immer wieder erreichen mich viele Anfragen von Eltern, die gern ein Kind aus Indien adoptieren wollen...</p></div>
        </article>
        <article class="tweet">
          <div class="avatar" role="img" aria-label="Profile photo"></div>
          <div><h3>Lena Brandt</h3><p>Immer wieder erreichen mich viele Anfragen von Eltern, die gern ein Kind aus Indien adoptieren wollen...</p></div>
        </article>
      </div>
      <a class="more" href="#">View more tweets</a>
    </section>

    <div class="closing-rule"></div>
  </main>

  <footer class="site-footer">
    <p>© marlene vogtberg © 2014 | Privacy Policy</p>
    <div class="social">
      <span class="facepage" aria-label="Facepage"></span>
      <span class="chirpnet" aria-label="Chirpnet"></span>
      <span class="globecircle" aria-label="Globecircle"></span>
    </div>
  </footer>
</body>
</html>
```